Dorvelan Swimming & Athletics Center

We need Business Card for a Athletics center
The logo frome the Uploaded Files ( b card fimal)
Οn one side of card we need the logo of company the Contact and the website:
1. Address:(Limassol, Cyprus 12-14 Stavrinelou str,Ano Trimeni,P.C. 4832)

2.Phone number: (+357) 25-704263

3. Mail: info@dorvelanfit.example

3. Website: www.dorvelanfit.example

Οn the other side of the card we need to write the sport of the company:

1. Artistic Gymnastics
2. Swimming
3. Gym - Fitness
4. Programs
5. Dancing
5.Tennis

From the Uploaded Files you can get the logo.In a logo is behind the black color which can be removed from logo.

Υou can use that color you want.
.
Updates

Industry/Entity Type

Business

Font styles to use
Decorative

Colors
0555a3
ffcf3e
3176b5
0692cd
add136
f04a50
000000
cfcfcf
9d9d9d

Requirements
Should not have
• photos with faces
• photo fro the Website:www.dorvelanfit.example

```html
<!DOCTYPE html>
<html lang="en">
<head>
<meta charset="utf-8">
<title>Dorvelan Athletics Center – Business Card</title>
<link rel="stylesheet" href="https://fonts.googleapis.com/css2?family=Archivo+Black&family=Open+Sans:wght@400;600&display=swap">
<style>
  :root {
    --backdrop: #e9e7e4;
    --paper: #ffffff;
    --navy: #0f2642;
    --gold: #f7b733;
    --gold-deep: #f0a81e;
    --ink: #2a2a2a;
    --night: #14151c;
    --snow: #f2f2f2;
  }
  * { box-sizing: border-box; margin: 0; padding: 0; }
  html, body {
    width: 1200px; height: 900px; overflow: hidden;
    background: var(--backdrop);
  }
  .canvas { position: relative; width: 1200px; height: 900px; }

  /* Front side */
  .card-front {
    position: absolute; left: 77px; top: 34px;
    width: 589px; height: 364px;
    background: var(--paper);
    box-shadow: 0 6px 18px rgba(0,0,0,.18);
    font-family: "Open Sans", Arial, sans-serif;
  }
  .card-front .band {
    position: absolute; left: 0; top: 61px;
    width: 100%; height: 109px;
    background: var(--navy);
  }
  .card-front .emblem {
    position: absolute; left: 193px; top: 20px;
    width: 190px; height: 190px; border-radius: 50%;
    background: var(--paper);
    display: flex; align-items: center; justify-content: center;
  }
  .emblem-name {
    font-family: "Archivo Black", "Arial Black", sans-serif;
    font-size: 26px; color: var(--navy); letter-spacing: .5px;
  }
  .address-block {
    position: absolute; left: 44px; top: 225px;
    color: var(--ink); font-size: 15.5px; line-height: 21.5px;
  }
  .address-block .company {
    color: var(--gold); font-weight: 600; font-size: 15px;
    margin-bottom: 3px; letter-spacing: .1px;
  }
  .contact-list {
    position: absolute; right: 40px; top: 242px;
    list-style: none; color: var(--ink);
    font-size: 15.5px; line-height: 21.5px; text-align: right;
  }
  .contact-list li { display: flex; align-items: center; justify-content: flex-end; gap: 8px; }
  .contact-list svg { width: 12px; height: 12px; fill: var(--gold); flex: none; }

  /* Back side */
  .card-back {
    position: absolute; left: 388px; top: 505px;
    width: 567px; height: 352px;
    background: var(--night);
    box-shadow: 0 6px 18px rgba(0,0,0,.25);
    font-family: "Open Sans", Arial, sans-serif;
  }
  .wordmark {
    position: absolute; left: 72px; top: 133px;
    display: flex; align-items: center; gap: 20px;
  }
  .wordmark-name {
    font-family: "Archivo Black", "Arial Black", sans-serif;
    font-size: 54px; line-height: 1; color: var(--gold-deep); letter-spacing: 1px;
  }
  .wordmark-disc {
    width: 76px; height: 76px; border-radius: 50%;
    border: 3px solid var(--snow); background: var(--gold-deep);
  }
  .sports {
    position: absolute; left: 0; top: 252px; width: 100%;
    color: var(--snow); font-size: 15.5px; line-height: 21px; text-align: center;
  }
  .sports-row { display: flex; justify-content: center; gap: 10px; }
  .sport { display: inline-flex; align-items: center; gap: 5px; }
  .sport::before {
    content: ""; width: 13px; height: 13px; border-radius: 50%;
    background: var(--gold); display: inline-block;
  }
</style>
</head>
<body>
<main class="canvas">

  <section class="card-front" aria-label="Business card front">
    <div class="band"></div>
    <div class="emblem"><span class="emblem-name">DORVELAN</span></div>

    <address class="address-block" style="font-style:normal">
      <p class="company">DORVELAN ATHLETICS CENTER</p>
      <p>Limassol, Cyprus 12-14</p>
      <p>Stavrinelou str,</p>
      <p>Ano Trimeni,P.C. 4832</p>
    </address>

    <ul class="contact-list">
      <li>(+357) 25-704263
        <svg viewBox="0 0 12 12"><path d="M1 4.5C1 2.5 3 1.5 6 1.5s5 1 5 3L9 5V4H3v1zM2.5 6h7l1 4.5h-9z"/></svg>
      </li>
      <li>info@dorvelanfit.example
        <svg viewBox="0 0 12 12"><path d="M1 3h10v6H1z M1 3l5 3.5L11 3" stroke="#fff" stroke-width=".8"/></svg>
      </li>
      <li>www.dorvelanfit.example
        <svg viewBox="0 0 12 12"><circle cx="6" cy="6" r="5"/><path d="M1 6h10M6 1c2 2 2 8 0 10M6 1c-2 2-2 8 0 10" stroke="#fff" stroke-width=".8" fill="none"/></svg>
      </li>
    </ul>
  </section>

  <section class="card-back" aria-label="Business card back">
    <div class="wordmark">
      <span class="wordmark-name">DORVELAN</span>
      <span class="wordmark-disc"></span>
    </div>
    <div class="sports">
      <div class="sports-row">
        <span class="sport">Artistic Gymnastics</span>
        <span class="sport">Swimming</span>
        <span class="sport">Tennis</span>
      </div>
      <div class="sports-row">
        <span class="sport">Gym - Fitness</span>
        <span class="sport">Programs</span>
        <span class="sport">Dancing</span>
      </div>
    </div>
  </section>

</main>
</body>
</html>
```